Ardenwell Building and Property Services needs a business card design

We need a business card design for our building and property services business. We already have a logo we just need a creative design and layout on a business card. Emphasis on clean, modern, professional.
Our client targets are mainly body corporates, building managers, construction managers.
We are a building services company that lean more to structural repair of buildings, through concrete rectification and carbon fibre strengthening.
We also refurbish facades, rendering, painting etc
We target higher end body corporates in prestigious locations, hence why we'd like our cards to reflect professionalism, strength, efficiency

Target Market(s)

body corporates, building managers, construction managers

Industry/Entity Type

Construction

Contact Information for Business Card

Ardenwell is the main word, with 'Building and Property Services' underneath.
Level 17, 82 Harlow Street
MERRIDALE
Melbourne
Vic 3094
T: 9518 2736
Duncan Ferris - Director
dunardenwell@mailbox-example.com

Requirements
Must have
• Stand out on the back of the card- strong/ bold, company logo
• All of the contact details written above
Should not have
• I'd like the card to stand out, especially on the back. Id like the company logo to be prominent, although feel free to be creative around it. But remain clean and professional

```html
<!DOCTYPE html>
<html lang="en">
<head>
<meta charset="utf-8">
<title>Ardenwell Building and Property Services – Business Card</title>
<link rel="stylesheet" href="https://fonts.googleapis.com/css2?family=Arimo:wght@400;700&display=swap">
<style>
  :root {
    --page-bg: #e9e6e1;
    --grey-light: #d9d9d9;
    --grey-mid: #9a9a9a;
    --grey-dark: #6b6b6b;
    --blue-light: #3fb4ee;
    --blue-mid: #1a8fd6;
    --blue-deep: #0a5e9e;
    --black-panel: #0d0d0e;
    --black-soft: #2a2a2c;
    --brand-blue: #2f9fe0;
    --white: #ffffff;
  }
  * { margin: 0; padding: 0; box-sizing: border-box; }
  html, body {
    width: 1200px; height: 950px; overflow: hidden;
    background: var(--page-bg);
    font-family: "Arimo", Arial, sans-serif;
  }
  .canvas { position: relative; width: 1200px; height: 950px; }
  .card {
    position: absolute; left: 220px; width: 760px; height: 420px;
    overflow: hidden;
    box-shadow: 0 10px 26px rgba(0,0,0,0.25);
  }
  /* Back of card */
  .card-back {
    top: 40px;
    background: radial-gradient(ellipse at 50% 35%, var(--grey-light) 0%, var(--grey-mid) 55%, var(--grey-dark) 100%);
    display: flex; align-items: center; justify-content: center;
  }
  .brand-name {
    font-weight: 700; color: var(--brand-blue);
    letter-spacing: 6px; text-transform: uppercase;
  }
  .card-back .brand-name { font-size: 64px; }

  /* Front of card */
  .card-front { top: 490px; background: var(--black-panel); }
  .front-shapes { position: absolute; inset: 0; width: 100%; height: 100%; }
  .contact {
    position: absolute; left: 42px; top: 34px; color: var(--white);
  }
  .contact-name { font-size: 26px; font-weight: 700; }
  .contact-role { font-size: 17px; margin-top: 4px; }
  .contact-address {
    font-size: 17px; line-height: 22px; margin-top: 88px;
  }
  .contact-list { list-style: none; margin-top: 14px; font-size: 16px; }
  .contact-list li { display: flex; align-items: center; gap: 10px; line-height: 26px; white-space: nowrap; }
  .contact-list svg { width: 16px; height: 16px; flex: none; }
  .brand-block {
    position: absolute; left: 400px; right: 0; top: 0; bottom: 0;
    display: flex; flex-direction: column; align-items: center; justify-content: center;
    padding-top: 60px; padding-left: 10px;
  }
  .card-front .brand-name { font-size: 40px; letter-spacing: 4px; }
  .brand-tagline {
    font-size: 10px; color: var(--brand-blue); letter-spacing: 1.5px;
    text-transform: uppercase; margin-top: 6px; white-space: nowrap;
  }
</style>
</head>
<body>
<main class="canvas">
  <section class="card card-back" aria-label="Card back">
    <span class="brand-name">Ardenwell</span>
  </section>

  <section class="card card-front" aria-label="Card front">
    <svg class="front-shapes" viewBox="0 0 760 420" preserveAspectRatio="none" aria-hidden="true">
      <defs>
        <radialGradient id="blueField" cx="0.25" cy="0.35" r="0.8">
          <stop offset="0" stop-color="#3fb4ee"/>
          <stop offset="0.6" stop-color="#1a8fd6"/>
          <stop offset="1" stop-color="#0a5e9e"/>
        </radialGradient>
        <linearGradient id="blackField" x1="0" y1="0" x2="1" y2="1">
          <stop offset="0" stop-color="#2a2a2c"/>
          <stop offset="0.5" stop-color="#0d0d0e"/>
          <stop offset="1" stop-color="#050505"/>
        </linearGradient>
      </defs>
      <rect class="blue-field" width="760" height="420" fill="url(#blueField)"/>
      <polygon class="bevel-edge" points="372,136 552,0 580,0 400,150 380,420 360,420" fill="#0a5e9e"/>
      <polygon class="black-panel" points="400,150 580,0 760,0 760,420 380,420" fill="url(#blackField)"/>
      <line x1="400" y1="150" x2="580" y2="0" stroke="#3fb4ee" stroke-width="2"/>
      <line x1="400" y1="150" x2="380" y2="420" stroke="#3fb4ee" stroke-width="2"/>
    </svg>

    <div class="contact">
      <p class="contact-name">Duncan Ferris</p>
      <p class="contact-role">Director</p>
      <p class="contact-address">Level 17, 82 Harlow Street<br>MERRIDALE, Melbourne<br>Vic 3094</p>
      <ul class="contact-list">
        <li>
          <svg viewBox="0 0 16 16" aria-hidden="true"><path fill="#fff" d="M3 2h3l1 3-2 1c1 2 2 3 4 4l1-2 3 1v3c0 1-1 2-2 2C6 14 2 10 2 4c0-1 0-2 1-2z"/></svg>
          9518 2736
        </li>
        <li>
          <svg viewBox="0 0 16 16" aria-hidden="true"><rect x="1" y="3" width="14" height="10" fill="#fff"/><path d="M1 3l7 6 7-6" fill="none" stroke="#1a8fd6" stroke-width="1.4"/></svg>
          dunardenwell@mailbox-example.com
        </li>
        <li>
          <svg viewBox="0 0 16 16" aria-hidden="true"><circle cx="8" cy="8" r="7" fill="#fff"/><path d="M1 8h14M8 1c3 3 3 11 0 14M8 1c-3 3-3 11 0 14" fill="none" stroke="#1a8fd6" stroke-width="1"/></svg>
          www.ardenwell-example.com
        </li>
      </ul>
    </div>

    <div class="brand-block">
      <span class="brand-name">Ardenwell</span>
      <span class="brand-tagline">Building and Property Services</span>
    </div>
  </section>
</main>
</body>
</html>
```